Wellness, weight management medical practice

We have a logo but want help designing and finalizing the business card. Japanese name. Will eventually be a holistic, full-service weight management and wellness center. Will be a virtual only practice to start.

```html
<!DOCTYPE html>
<html lang="en">
<head>
<meta charset="utf-8">
<title>Sora Hayashi Wellness – Business Cards</title>
<link rel="stylesheet" href="https://fonts.googleapis.com/css2?family=Lato:wght@400;700;900&family=Noto+Sans+JP:wght@400;700&display=swap">
<style>
  :root{
    --bg:#2e2e2e;
    --card:#ffffff;
    --gold-deep:#9a6f1f;
    --gold-light:#d5a743;
    --ink:#2b2b2b;
  }
  *{box-sizing:border-box;margin:0;padding:0}
  html,body{width:1200px;height:875px;overflow:hidden;background:var(--bg)}
  body{position:relative;font-family:"Lato",sans-serif}
  .card{
    position:absolute;left:280px;width:640px;height:366px;
    background:var(--card);border-radius:22px;overflow:hidden;
  }
  .card--jp{top:56px}
  .card--en{top:454px}
  .rule{position:absolute;left:50px;top:232px;width:540px;height:1.5px;background:var(--gold-deep)}
  .name{position:absolute;left:50px;top:150px;color:var(--gold-deep);font-weight:900;font-size:36px;letter-spacing:.5px;line-height:1}
  .role{position:absolute;left:52px;top:196px;color:var(--gold-light);font-size:19px;line-height:1}
  .card--jp .name{font-family:"Noto Sans JP",sans-serif;font-weight:700;font-size:34px}
  .card--jp .role{font-family:"Noto Sans JP",sans-serif;font-size:16px;top:200px}
  .contacts{position:absolute;left:50px;top:248px;list-style:none}
  .contacts li{display:flex;align-items:center;gap:10px;height:23px;color:var(--ink);font-size:16px}
  .contacts svg{width:13px;height:13px;flex:none}
  .brand{position:absolute;left:420px;top:30px;width:170px;height:170px}
  .brand__ring{position:absolute;inset:10px;border:3px solid var(--gold-light);border-radius:50%}
  .brand__name{position:absolute;inset:0;display:flex;align-items:center;justify-content:center;text-align:center;color:var(--gold-deep);font-size:17px;font-weight:400;line-height:1.3;letter-spacing:.5px}
  .office{position:absolute;right:50px;top:248px;text-align:right;font-size:15px;line-height:23px;color:var(--ink)}
  .office__company{color:var(--gold-light)}
  .card--jp .office{font-family:"Noto Sans JP",sans-serif;font-size:14px}
</style>
</head>
<body>

<section class="card card--jp" lang="ja">
  <div class="brand">
    <div class="brand__ring"></div>
    <div class="brand__name" lang="en">Sorahayashi<br>Wellness</div>
  </div>
  <h1 class="name">ソラ・ハヤシ</h1>
  <p class="role">ウェルネスプラクティス</p>
  <div class="rule"></div>
  <ul class="contacts" lang="en">
    <li><svg viewBox="0 0 16 16"><path d="M4 1l3 3-2 2c1 2 3 4 5 5l2-2 3 3-2 2C7 14 2 9 2 3z" fill="var(--gold-light)"/></svg>(555) 214-3870</li>
    <li><svg viewBox="0 0 16 16"><rect x="1" y="3" width="14" height="10" fill="var(--gold-light)"/><path d="M1 3l7 6 7-6" stroke="#fff" stroke-width="1.4" fill="none"/></svg>office@sorahayashi.com</li>
    <li><svg viewBox="0 0 16 16"><circle cx="8" cy="8" r="6.5" fill="none" stroke="var(--gold-light)" stroke-width="1.6"/><path d="M1.5 8h13M8 1.5c-3 3.5-3 9.5 0 13M8 1.5c3 3.5 3 9.5 0 13" stroke="var(--gold-light)" stroke-width="1.2" fill="none"/></svg>www.sorahayashi.com</li>
  </ul>
  <address class="office" style="font-style:normal">
    <div class="office__company">ソラ・ハヤシ・ウェルネス</div>
    <div>あなたの住所、市</div>
    <div>州、郵便番号 1235</div>
  </address>
</section>

<section class="card card--en">
  <div class="brand">
    <div class="brand__ring"></div>
    <div class="brand__name">Sorahayashi<br>Wellness</div>
  </div>
  <h1 class="name">SORA HAYASHI</h1>
  <p class="role">Wellnes Practice</p>
  <div class="rule"></div>
  <ul class="contacts">
    <li><svg viewBox="0 0 16 16"><path d="M4 1l3 3-2 2c1 2 3 4 5 5l2-2 3 3-2 2C7 14 2 9 2 3z" fill="var(--gold-light)"/></svg>(555) 214-3870</li>
    <li><svg viewBox="0 0 16 16"><rect x="1" y="3" width="14" height="10" fill="var(--gold-light)"/><path d="M1 3l7 6 7-6" stroke="#fff" stroke-width="1.4" fill="none"/></svg>office@sorahayashi.com</li>
    <li><svg viewBox="0 0 16 16"><circle cx="8" cy="8" r="6.5" fill="none" stroke="var(--gold-light)" stroke-width="1.6"/><path d="M1.5 8h13M8 1.5c-3 3.5-3 9.5 0 13M8 1.5c3 3.5 3 9.5 0 13" stroke="var(--gold-light)" stroke-width="1.2" fill="none"/></svg>www.sorahayashi.com</li>
  </ul>
  <address class="office" style="font-style:normal">
    <div class="office__company">Sora Hayashi Wellness</div>
    <div>Your Address, City</div>
    <div>State, Zip 1235</div>
  </address>
</section>

</body>
</html>
```